依頼概要
■依頼の目的/概要
小学生バレーボールのスポーツ少年団でメンバーを募集するためのポスターの作成をお願いします。

■依頼詳細
ポスターは男子チーム、女子チーム兼用となります。主に教室での直接配布、校内の掲示板や近隣の施設(コンビニや公民館等)での掲示を目的としたものになります。

必要に応じて写真の背景等を加工いただいても構いません。

楽しそうなイメージだけでなく、スポーツに関心のある子どもたちがバレーボールを“かっこいい”と感じてくれるような躍動感の伝わるものを希望しています。

■重視する点
・明るくインパクトのあるデザイン
・できるだけ躍動感の伝わるもの
・読みやすい文字であること

■サイズ
A4サイズでお願いします。
メインはA4ですが、B4(A4の122%)にも対応する画素数でお願いいたします

■その他
・レイアウトイメージ、素材は添付ファイルにてご確認ください
・写真やイラストの素材は当方で用意していますが、用意したもの以外の素材を使っていただいても構いません。
・レイアウトのイメージやキャッチコピー、掲載する文言等は添付の「レイアウトイメージ.pdf」「レイアウト説明.txt」を参照ください。レイアウトは当方のイメージと異なるものになっても構いません。

何かご不明な点がございましたら、お気軽にご質問下さい。
どうぞよろしくお願いいたします。
納品いただくデータですが、納品後に当方で編集することがあるため、フォトショップまたはイラストレーターで編集できるかたちで納品いただけますと幸いです。よろしくお願いします。

```html
<!DOCTYPE html>
<html lang="ja">
<head>
<meta charset="utf-8">
<title>青空バレースポーツ少年団 メンバー募集</title>
<link rel="stylesheet" href="https://fonts.googleapis.com/css2?family=M+PLUS+1p:wght@500;700;800;900&family=Kiwi+Maru:wght@500&display=swap">
<style>
  :root {
    --red: #d5161e;
    --red-dark: #a80f16;
    --navy: #1b2f7a;
    --yellow: #ffe600;
    --white: #ffffff;
    --ink: #222222;
  }
  * { margin: 0; padding: 0; box-sizing: border-box; }
  html, body { width: 846px; height: 1200px; overflow: hidden; background: var(--white); }
  .poster {
    position: relative; width: 846px; height: 1200px; overflow: hidden;
    font-family: "M PLUS 1p", sans-serif; color: var(--ink); background: var(--white);
  }
  .hero { position: absolute; left: 0; top: 0; width: 846px; height: 705px; background: var(--red); }
  .photo { position: absolute; }
  .photo--receive { left: 0; top: 0; width: 370px; height: 270px; background: linear-gradient(135deg, #c9b79a, #8d6f55 60%, #b52a2f); }
  .photo--huddle { left: 565px; top: 78px; width: 281px; height: 262px; background: linear-gradient(160deg, #d8d2c8, #9c8a7a 55%, #c0303a); }
  .photo--gym { left: 0; top: 282px; width: 318px; height: 228px; background: linear-gradient(180deg, #f1ede6, #d9cfc1); }
  .photo--safety { left: 525px; top: 300px; width: 321px; height: 190px; background: linear-gradient(135deg, #c7c0b5, #8a7c70 60%, #4a4f7a); }
  .photo--group { left: 255px; top: 540px; width: 591px; height: 165px; background: linear-gradient(180deg, #d3cbc0, #a14452 60%, #6b2a35); }

  .note {
    position: absolute; font-family: "Kiwi Maru", sans-serif; font-weight: 500;
    line-height: 1.15; white-space: nowrap;
    paint-order: stroke fill; -webkit-text-stroke: 6px var(--navy);
  }
  .note--receive { left: 14px; top: 14px; color: var(--yellow); font-size: 34px; transform: rotate(-8deg); }
  .note--friends { left: 612px; top: 24px; color: var(--yellow); font-size: 30px; transform: rotate(-6deg); text-align: center; }
  .note--indoor { left: 18px; top: 420px; color: var(--red); font-size: 26px; -webkit-text-stroke: 6px var(--white); transform: rotate(-4deg); }
  .note--safety { left: 640px; top: 432px; color: var(--white); font-size: 24px; -webkit-text-stroke: 5px var(--red-dark); }

  .headline {
    position: absolute; left: 0; top: 195px; width: 846px; text-align: center;
    font-weight: 900; color: var(--white); line-height: 1.12; letter-spacing: -2px;
    paint-order: stroke fill; -webkit-text-stroke: 14px var(--navy);
  }
  .headline__line { display: block; }
  .headline__line--a { font-size: 84px; }
  .headline__line--b { font-size: 112px; letter-spacing: -6px; }
  .headline__line--c { font-size: 96px; }

  .recruit {
    position: absolute; left: 0; top: 712px; width: 846px; text-align: center;
    font-weight: 900; color: var(--yellow); line-height: 1.12;
    paint-order: stroke fill; -webkit-text-stroke: 10px var(--navy);
  }
  .recruit__team { display: block; font-size: 52px; }
  .recruit__call { display: block; font-size: 62px; }

  .photo--kids { left: 14px; top: 838px; width: 210px; height: 125px; background: linear-gradient(160deg, #b7c4d8, #e8c6a8 60%, #7b8f6a); }
  .mascot { position: absolute; left: 612px; top: 836px; width: 210px; height: 140px; border-radius: 40px; background: linear-gradient(180deg, #e7ece9, #b9c6c0); }

  .message { position: absolute; left: 230px; top: 846px; width: 380px; text-align: center; font-weight: 800; line-height: 1.3; }
  .message__sub { display: block; font-size: 17px; color: var(--navy); }
  .message__main { display: block; font-size: 27px; color: var(--red); margin-bottom: 4px; }

  .schedule { position: absolute; left: 14px; top: 972px; width: 818px; height: 88px; display: flex; border: 3px solid var(--navy); }
  .schedule__label { width: 112px; background: var(--navy); color: var(--white); display: flex; flex-direction: column; justify-content: center; align-items: center; font-weight: 900; font-size: 24px; line-height: 1.2; }
  .schedule__label small { font-size: 15px; }
  .schedule__rows { flex: 1; display: flex; flex-direction: column; justify-content: center; padding-left: 16px; }
  .schedule__row { display: flex; font-size: 21px; font-weight: 700; color: var(--ink); line-height: 1.6; }
  .schedule__day { width: 140px; color: var(--navy); font-weight: 900; }

  .notice { position: absolute; left: 0; top: 1068px; width: 846px; height: 54px; display: flex; align-items: center; justify-content: center; }
  .notice::before { content: ""; position: absolute; left: 14px; right: 14px; bottom: 6px; height: 14px; background: var(--red); }
  .notice__text { position: relative; font-size: 36px; font-weight: 900; color: var(--navy); paint-order: stroke fill; -webkit-text-stroke: 6px var(--white); }

  .footer { position: absolute; left: 14px; top: 1130px; width: 818px; height: 60px; display: flex; justify-content: space-between; align-items: center; }
  .items { display: flex; flex-direction: column; gap: 4px; }
  .items__row { display: flex; align-items: center; gap: 8px; font-size: 16px; font-weight: 700; }
  .items__tag { background: var(--navy); color: var(--white); padding: 2px 10px; border-radius: 12px; font-size: 14px; }
  .items__contact { color: var(--red); font-size: 16px; font-weight: 800; }
  .contact { display: flex; align-items: center; gap: 10px; }
  .contact__tag { background: var(--navy); color: var(--white); padding: 4px 8px; font-size: 14px; font-weight: 800; writing-mode: vertical-rl; }
  .contact__body { line-height: 1.15; }
  .contact__org { font-size: 16px; font-weight: 700; }
  .contact__tel { display: flex; align-items: center; gap: 4px; font-size: 34px; font-weight: 900; color: var(--red); }
  .contact__tel svg { width: 26px; height: 26px; }
</style>
</head>
<body>
<main class="poster">
  <section class="hero">
    <div class="photo photo--receive" role="img" aria-label="体育館でレシーブする子どもたちの写真"></div>
    <div class="photo photo--huddle" role="img" aria-label="円陣を組むチームの写真"></div>
    <div class="photo photo--gym" role="img" aria-label="屋内体育館で練習する様子の写真"></div>
    <div class="photo photo--safety" role="img" aria-label="練習中のチームの写真"></div>
    <div class="photo photo--group" role="img" aria-label="ユニフォーム姿のチーム集合写真"></div>

    <p class="note note--receive">レシーブ、スパイク!<br>きっと気もちいい!</p>
    <p class="note note--friends">チームのみんな<br>仲よし!<br>楽しいよう!</p>

    <h1 class="headline">
      <span class="headline__line headline__line--a">そうだ、</span>
      <span class="headline__line headline__line--b">バレーボール、</span>
      <span class="headline__line headline__line--c">しよう。</span>
    </h1>

    <p class="note note--indoor">屋内だから<br>夏場や雨の日も<br>安心!!</p>
    <p class="note note--safety">感染症対策<br>もしています。</p>
  </section>

  <h2 class="recruit">
    <span class="recruit__team">青空バレースポーツ少年団</span>
    <span class="recruit__call">男女新メンバー募集!!</span>
  </h2>

  <div class="photo photo--kids" role="img" aria-label="笑顔の団員たちの写真"></div>
  <p class="message">
    <span class="message__sub">みんなが下のなまえでよびあう青空バレーは</span>
    <span class="message__main">仲のよさがじまん!</span>
    <span class="message__sub">いろいろな小学校から集まっているから</span>
    <span class="message__main">友だちもたくさんできるよ!</span>
  </p>
  <div class="mascot" role="img" aria-label="バレーボールのマスコットキャラクターのイラスト"></div>

  <section class="schedule">
    <div class="schedule__label">練習日<small>(毎週)</small></div>
    <div class="schedule__rows">
      <p class="schedule__row"><span class="schedule__day">土・日曜日</span>青空小学校体育館・青空西小学校体育館 9:00〜</p>
      <p class="schedule__row"><span class="schedule__day">水 曜 日</span>青空小学校体育館 17:30〜</p>
    </div>
  </section>

  <div class="notice"><p class="notice__text">見学・体験はいつでも受け付けています!</p></div>

  <footer class="footer">
    <div class="items">
      <p class="items__row"><span class="items__tag">持ち物</span>上ぐつ、水とう、動きやすい服そう</p>
      <p class="items__contact">連絡は右記の携帯電話まで</p>
    </div>
    <div class="contact">
      <span class="contact__tag">連絡先</span>
      <div class="contact__body">
        <p class="contact__org">青空バレースポーツ少年団 育成会会長 森田</p>
        <p class="contact__tel">
          <svg viewBox="0 0 24 24" aria-hidden="true"><path fill="#d5161e" d="M6.6 10.8a15.1 15.1 0 0 0 6.6 6.6l2.2-2.2a1 1 0 0 1 1-.25 11.4 11.4 0 0 0 3.6.57 1 1 0 0 1 1 1V20a1 1 0 0 1-1 1A17 17 0 0 1 3 4a1 1 0 0 1 1-1h3.5a1 1 0 0 1 1 1c0 1.25.2 2.450.57 3.6a1 1 0 0 1-.25 1z"/></svg>
          TEL 090-XXX-XXXX
        </p>
      </div>
    </div>
  </footer>
</main>
</body>
</html>
```